New Web Design Project for kids music school

We need a homepage mockup for a kids' music program. Use your creative talent to come up with something visually appeal and professional for this web-site.

More information is provided in the PDF file called HOME. Also included in this file are links to the photos to be used.

Please let me know if you have more questions.

Target Market(s)

parents

Number of Pages Required

1 page

Font styles to use
Sans Serif

```html
<!DOCTYPE html>
<html lang="en">
<head>
<meta charset="utf-8">
<title>Little Notes! – Live Music Education for Kids</title>
<link rel="stylesheet" href="https://fonts.googleapis.com/css2?family=Roboto:wght@400;500;700;900&family=Rubik:wght@700;800&display=swap">
<style>
:root{
  --purple:#3f37a8;
  --purple-deep:#3a2f9e;
  --purple-grey:#5a588c;
  --royal:#2a1fc0;
  --lime:#c9cc45;
  --lime-text:#e4e46a;
  --olive-text:#cfcd55;
  --white:#ffffff;
  --header:rgba(236,236,205,0.9);
  --red:#e0352b;
}
*{margin:0;padding:0;box-sizing:border-box}
html,body{width:1200px;height:5013px;overflow:hidden}
body{position:relative;font-family:"Roboto",Arial,sans-serif;background:var(--purple)}
.abs{position:absolute}
.center-text{left:0;width:1200px;text-align:center}

/* hero */
.hero-photo{left:0;top:0;width:1200px;height:680px;background:linear-gradient(160deg,#c9cfa2 0%,#d9a7b5 45%,#8e6a8c 75%,#6e6a86 100%)}
.hero-wedge{left:0;top:0;width:1200px;height:680px}
.site-header{left:0;top:0;width:1200px;height:160px;background:var(--header)}
.brand{left:97px;top:70px;font-family:"Rubik",sans-serif;font-weight:800;font-size:40px;color:var(--royal);line-height:1}
.nav-link{top:92px;font-size:15px;font-weight:500;color:var(--royal);letter-spacing:.3px}
.nav-phone{left:856px;top:86px;font-size:21px;color:var(--royal)}
.phone-icon{left:1062px;top:82px;width:30px;height:30px}

/* bands */
.band{left:0;width:1200px;background:var(--lime)}
.band-intro{top:680px;height:150px}
.band-title{top:700px;font-size:41px;font-weight:700;color:var(--royal)}
.band-sub{top:762px;font-size:37px;font-weight:700;color:var(--royal)}

/* programs section */
.programs{left:0;top:830px;width:1200px;height:2292px;background:linear-gradient(180deg,#4a40aa 0%,#3d33ad 100%)}
.programs-shapes{left:0;top:830px;width:1200px;height:2292px}
.intro-line{top:900px;font-size:38px;font-weight:500;color:var(--lime-text)}
.intro-age{top:970px;font-size:50px;font-weight:500;color:var(--lime-text);letter-spacing:.5px}
.btn{background:var(--white);color:var(--royal);font-weight:700;border-radius:12px;text-align:center;box-shadow:0 4px 10px rgba(0,0,0,.25)}
.btn-signup{left:519px;top:1076px;width:152px;height:62px;line-height:62px;font-size:25px}
.program-box{border:2px solid rgba(255,255,255,.75);text-align:center;font-family:"Rubik",sans-serif}
.program-title{display:block;color:var(--lime-text);font-weight:800;font-size:35px;margin-top:18px;letter-spacing:.3px}
.program-age{display:block;color:var(--white);font-weight:800;font-size:27px;margin-top:6px}
.box-live{left:105px;top:1218px;width:523px;height:132px}
.box-stars{left:403px;top:2106px;width:696px;height:133px}
.photo{box-shadow:0 6px 16px rgba(0,0,0,.3)}
.photo-live{left:105px;top:1398px;width:823px;height:368px;background:linear-gradient(135deg,#9fb48e 0%,#d7c7b0 40%,#9aa2b8 75%,#6b7180 100%)}
.photo-stars{left:278px;top:2289px;width:821px;height:374px;background:linear-gradient(135deg,#2b1c20 0%,#b8242e 35%,#2f7a44 65%,#d4b2a2 100%)}
.program-copy{font-size:23px;font-weight:500;line-height:43.5px;color:var(--lime-text)}
.copy-live{left:105px;top:1806px;width:880px}
.copy-stars{left:200px;top:2705px;width:896px;text-align:right}
.btn-learn{height:43px;line-height:43px;font-size:18px;width:138px;border-radius:14px}
.learn-live{left:103px;top:2005px}
.learn-stars{left:959px;top:2904px}
.virtual-heading{top:3028px;font-size:46px;font-weight:700;color:var(--olive-text)}

.band-virtual{top:3122px;height:150px}
.virtual-line{top:3143px;font-size:40px;font-weight:500;color:var(--royal);line-height:59px}

/* media section */
.media{left:0;top:3272px;width:1200px;height:1420px;background:linear-gradient(180deg,#3b319f 0%,#37309c 100%)}
.video-dot{left:594px;top:3360px;width:54px;height:54px;border-radius:50%;background:var(--red)}
.media-heading{font-size:43px;font-weight:700;color:var(--olive-text)}
.videos-heading{top:3460px}
.video-frame{left:335px;top:3551px;width:544px;height:296px;border:2px solid #d8d8e6;background:linear-gradient(180deg,#c9c0b0 0%,#b7a89a 50%,#6f5b55 100%)}
.video-bar{left:337px;top:3815px;width:540px;height:30px;background:rgba(0,0,0,.55)}
.follow-square{left:366px;top:3970px;width:74px;height:74px;border-radius:16px;background:#d8407a}
.follow-heading{left:457px;top:3987px}
.feed-photo{width:227px;height:228px;border:2px solid #e6e6ee}
.feed-1{left:195px;top:4086px;background:linear-gradient(135deg,#c9a58e,#7fa0b8)}
.feed-2{left:482px;top:4086px;background:linear-gradient(135deg,#a27a5a,#d8b7b0)}
.feed-3{left:768px;top:4086px;background:linear-gradient(135deg,#4a4a55,#c8c3c0)}
.feed-4{left:191px;top:4361px;background:linear-gradient(135deg,#b99884,#7a5c78)}
.feed-5{left:484px;top:4361px;background:linear-gradient(135deg,#9ea0a6,#5c6a84)}
.feed-6{left:778px;top:4361px;background:linear-gradient(135deg,#c76b8c,#7d5a9a)}

/* footer */
.site-footer{left:0;top:4692px;width:1200px;height:321px;background:var(--lime)}
.footer-line{left:193px;font-size:17px;font-weight:700;color:var(--royal)}
.footer-fine{left:193px;font-size:13px;font-weight:700;color:var(--royal)}
.social-square{top:4850px;width:38px;height:38px;border:3px solid var(--royal);border-radius:6px}
.footer-brand{left:612px;top:4790px;font-family:"Rubik",sans-serif;font-weight:800;font-size:76px;color:var(--royal);line-height:1}
</style>
</head>
<body>

<div class="abs hero-photo" role="img" aria-label="Photo of excited young children sitting on a classroom floor with their arms raised"></div>
<svg class="abs hero-wedge" viewBox="0 0 1200 680" aria-hidden="true"><polygon points="0,496 545,680 0,680" fill="#5a5590"/></svg>

<header class="abs site-header">
  <div class="abs brand">Little Notes!</div>
  <nav>
    <span class="abs nav-link" style="left:414px">HOME</span>
    <span class="abs nav-link" style="left:541px">PROGRAMS</span>
    <span class="abs nav-link" style="left:706px">CONTACT</span>
    <span class="abs nav-phone">+1 (555) 014-2290</span>
    <svg class="abs phone-icon" viewBox="0 0 24 24" aria-hidden="true"><path fill="#2a1fc0" d="M6.6 10.8a15.1 15.1 0 0 0 6.6 6.6l2.2-2.2c.3-.3.7-.4 1-.2 1.1.4 2.3.6 3.6.6.6 0 1 .4 1 1V20c0 .6-.4 1-1 1A17 17 0 0 1 3 4c0-.6.4-1 1-1h3.5c.6 0 1 .4 1 1 0 1.3.2 2.5.6 3.6.1.3 0 .7-.2 1z"/></svg>
  </nav>
</header>

<section>
  <div class="abs band band-intro"></div>
  <h1 class="abs center-text band-title">LIVE MUSIC EDUCATION &amp; THE STARS!</h1>
  <p class="abs center-text band-sub">Performing Program</p>
</section>

<section>
  <div class="abs programs"></div>
  <svg class="abs programs-shapes" viewBox="0 0 1200 2292" aria-hidden="true">
    <polygon points="0,726 1200,1212 1200,2292 0,2292" fill="#58568c"/>
    <polygon points="778,0 1200,0 1200,143" fill="#ffffff"/>
  </svg>

  <p class="abs center-text intro-line">Programs available for kids</p>
  <p class="abs center-text intro-age">3 MONTHS TO 14 YEARS OLD</p>
  <div class="abs btn btn-signup">SIGN UP!</div>

  <div class="abs program-box box-live">
    <span class="program-title">LIVE MUSIC PROGRAM</span>
    <span class="program-age">3 MOS. - 3 YRS.</span>
  </div>
  <div class="abs photo photo-live" role="img" aria-label="Photo of toddlers dancing with arms raised in a bright music classroom"></div>
  <p class="abs program-copy copy-live">This “mommy &amp; me” style class is a 45 minute live music adventure. Each class has a singer and pianist guiding little ones through 3 boxes of instruments built for their little hands. We use music to teach movement, vocabulary, numbers, letters, confidence and build a love of music.</p>
  <div class="abs btn btn-learn learn-live">Learn More</div>

  <div class="abs program-box box-stars">
    <span class="program-title">STARS! PERFORMANCE PROGRAM</span>
    <span class="program-age">3 - 14 YRS.</span>
  </div>
  <div class="abs photo photo-stars" role="img" aria-label="Photo of a group of children in holiday elf costumes on stage"></div>
  <p class="abs program-copy copy-stars">Kids work once a week to put on a show customized for their class. Every child has a solo, lines, and a big part. We have classes for kids ages 3-14. Our mission is confidence and teaching important life skills through theater. All classes perform their show at the end of the session.</p>
  <div class="abs btn btn-learn learn-stars">Learn More</div>

  <h2 class="abs center-text virtual-heading">VIRTUAL MUSIC LESSONS</h2>
</section>

<section>
  <div class="abs band band-virtual"></div>
  <p class="abs center-text virtual-line">We’re now offering one on one virtual<br>music lessons</p>
</section>

<section>
  <div class="abs media"></div>
  <div class="abs video-dot"></div>
  <h2 class="abs center-text media-heading videos-heading">OUR LATEST CLIPSTREAM VIDEOS</h2>
  <div class="abs video-frame" role="img" aria-label="Video still of a music teacher speaking to the camera in a classroom"></div>
  <div class="abs video-bar"></div>

  <div class="abs follow-square"></div>
  <h2 class="abs media-heading follow-heading">FOLLOW US ON SNAPLINE</h2>
  <div class="abs feed-photo feed-1" role="img" aria-label="Feed photo of two teachers holding a book"></div>
  <div class="abs feed-photo feed-2" role="img" aria-label="Feed photo of a toddler playing on a floor mat"></div>
  <div class="abs feed-photo feed-3" role="img" aria-label="Feed photo of children watching a lesson on a TV"></div>
  <div class="abs feed-photo feed-4" role="img" aria-label="Feed photo of a child following a lesson on a tablet"></div>
  <div class="abs feed-photo feed-5" role="img" aria-label="Collage of kids joining virtual lessons at home"></div>
  <div class="abs feed-photo feed-6" role="img" aria-label="Feed photo of two girls hugging"></div>
</section>

<footer class="abs site-footer">
  <p class="abs footer-line" style="top:40px">14 MAPLE GROVE RD. FAIRVIEW, MA 01999</p>
  <p class="abs footer-line" style="top:83px">(555) 014-2290</p>
  <p class="abs footer-line" style="top:126px">INFO@LITTLENOTESMUSIC.COM</p>
  <div class="abs social-square" style="left:193px;top:158px"></div>
  <div class="abs social-square" style="left:252px;top:158px"></div>
  <p class="abs footer-fine" style="top:226px">COPYRIGHT © 2020 LITTLE NOTES!. ALL RIGHTS RESERVED.</p>
  <p class="abs footer-fine" style="top:261px">PHOTOS TAKEN BY DANA WHITFIELD</p>
  <div class="abs footer-brand" style="top:90px">Little<br>Notes!</div>
</footer>

</body>
</html>
```